Cover-Design für CD gesucht
Zielgruppe
Ich bin eine Pianistin. Ich habe klassische Musik aufgenommen von Brokk, Tumsat, Falkenor, Quirnbacher, Gelvat… Alle Wasserstücke! Das Konzept ist Natur und Musik.
Grundsätzlich möchte gerne meine ausgewählte Fotos für design verwenden. Bitte eleganter, geschmackvolerl, edeler und klassischer Stil mag ich gerne haben.
Die Zielgruppe ist klassische Musik.
Aufgabenstellung
Wir wünschen uns etwas antiken & anmutigen Stil.
Die CD form ist 'CD-Digipack 4-seitig, 1Tray rechts mit Bookletschlitz links' für das Booklet möchte ich
4 Seiten.
Ich möchte für CD Design viel meine Fotos benutzen, aber auch dazu bitte Text anpassen:))
Texte und Fotos mit der Seiten Beschreibungen sehen Sie bitte die Dateien als Anhang!
Bitte Innere Seiten von CD Cover mit Bookletschlitz und CD Tray wünsche ich auch etwas geschmackvoll und passende design!

```html
<!DOCTYPE html>
<html lang="de">
<head>
<meta charset="utf-8">
<title>Wasser – Digipack Entwurf</title>
<link rel="stylesheet" href="https://fonts.googleapis.com/css2?family=Encode+Sans+Condensed:wght@400;500&family=Noto+Sans+JP:wght@300;400&family=Playfair+Display:wght@900&family=Cinzel:wght@700&display=swap">
<style>
  :root {
    --frame: #c5dcf3;
    --ink: #7d8fa6;
    --ink-soft: #8797ab;
    --title: #c3e0ea;
    --title-deep: #a9cfdc;
    --number: #b9d6ee;
    --panel-white: #fbfcfd;
  }
  * { margin: 0; padding: 0; box-sizing: border-box; }
  html, body { width: 1200px; height: 1076px; overflow: hidden; background: var(--frame); }
  .sheet { position: relative; width: 1200px; height: 1076px; background: var(--frame); }

  .spread { position: absolute; left: 13px; width: 1169px; height: 513px; display: flex; }
  .spread--one { top: 13px; }
  .spread--two { top: 545px; }

  .back-panel { position: relative; width: 572px; height: 513px; overflow: hidden; }
  .front-panel { position: relative; width: 597px; height: 513px; overflow: hidden; background: var(--panel-white); }

  .photo-lake {
    position: absolute; inset: 0;
    background:
      radial-gradient(ellipse 22% 45% at 74% 62%, rgba(120,90,70,.35), transparent 70%),
      radial-gradient(ellipse 30% 30% at 62% 80%, rgba(235,230,215,.9), transparent 70%),
      linear-gradient(180deg, #f6f7f2 0%, #eef0e8 35%, #e3e6dc 55%, #d9dccf 75%, #b9b4a6 88%, #8f8a80 100%);
  }
  .photo-portrait {
    position: absolute; inset: 0;
    background:
      radial-gradient(ellipse 30% 44% at 42% 36%, rgba(110,100,120,.55), transparent 70%),
      radial-gradient(ellipse 26% 30% at 72% 82%, rgba(120,165,135,.55), transparent 72%),
      radial-gradient(ellipse 40% 30% at 40% 80%, rgba(205,222,242,.8), transparent 70%),
      linear-gradient(90deg, #e9eef5 0%, #f4f7fb 45%, var(--panel-white) 70%);
  }

  .track { position: absolute; }
  .track__jp { left: 47px; width: 124px; font-family: "Noto Sans JP", sans-serif; color: var(--ink); }
  .track__en { left: 176px; font-family: "Encode Sans Condensed", sans-serif; color: var(--ink); }
  .track__name { font-size: 15px; line-height: 20px; font-weight: 300; letter-spacing: 0; white-space: nowrap; }
  .track__en .track__name { font-weight: 400; font-size: 16.5px; }
  .track__works { font-size: 8.5px; line-height: 12px; margin-top: 2px; white-space: nowrap; }
  .track__jp .track__works { font-weight: 400; }

  .contact { position: absolute; left: 47px; top: 357px; font-family: "Encode Sans Condensed", sans-serif; color: var(--ink); font-size: 13px; line-height: 15px; }

  .title { position: absolute; left: 330px; width: 200px; text-align: center; color: var(--title); }
  .title__kanji { font-family: "Noto Sans JP", sans-serif; font-weight: 400; font-size: 38px; line-height: 40px; top: 76px; }
  .title__word { top: 120px; line-height: 46px; color: var(--title-deep); }
  .title__word--serif { font-family: "Playfair Display", serif; font-weight: 900; font-size: 54px; letter-spacing: 1px; }
  .title__word--caps { font-family: "Cinzel", serif; font-weight: 700; font-size: 40px; left: 310px; width: 240px; letter-spacing: 1px; }

  .artist { position: absolute; left: 330px; width: 200px; text-align: center; color: var(--ink-soft); }
  .artist__en { top: 191px; font-family: "Encode Sans Condensed", sans-serif; font-size: 20px; }
  .artist__jp { top: 218px; font-family: "Noto Sans JP", sans-serif; font-weight: 300; font-size: 14px; letter-spacing: .5px; }

  .label { position: absolute; left: 60px; top: 408px; display: flex; align-items: center; gap: 6px;
    font-family: "Encode Sans Condensed", sans-serif; font-size: 15px; color: var(--ink-soft); }
  .label__dot { width: 8px; height: 8px; border-radius: 50%; background: var(--ink-soft); }
  .composers { position: absolute; left: 89px; top: 428px; font-family: "Encode Sans Condensed", sans-serif; font-size: 17px; line-height: 18.5px; color: var(--ink); }

  .disc-number { position: absolute; right: 12px; bottom: 10px; font-family: "Playfair Display", serif; font-weight: 900; font-size: 34px; font-variant-numeric: lining-nums; color: var(--number); }
</style>
</head>
<body>
<div class="sheet">

  <section class="spread spread--one">
    <div class="back-panel">
      <div class="photo-lake" role="img" aria-label="Foto: Pianistin im hellen Kleid liest Noten an einem Holzgeländer am nebligen See"></div>
      <div class="track track__jp" style="top:54px"><p class="track__name">ブロック</p><p class="track__works">エステ荘の噴水</p></div>
      <div class="track track__en" style="top:54px"><p class="track__name">F. Brokk</p><p class="track__works">Les jeux d'eaux à la Villa d'Este</p></div>
      <div class="track track__jp" style="top:93px"><p class="track__name">トゥムザット</p><p class="track__works">水の戯れ</p></div>
      <div class="track track__en" style="top:93px"><p class="track__name">M. Tumsat</p><p class="track__works">Jeux d'eau</p></div>
      <div class="track track__jp" style="top:133px"><p class="track__name">ファルケノール</p><p class="track__works">水の反映<br>雨の庭<br>金色の魚</p></div>
      <div class="track track__en" style="top:133px"><p class="track__name">C. Falkenor</p><p class="track__works">Reflets dans l'eau<br>Jardins sous la pluie<br>Poissons d'or</p></div>
      <div class="track track__jp" style="top:196px"><p class="track__name">ヴァレンヌ</p><p class="track__works">舟歌 第2番 ト長調</p></div>
      <div class="track track__en" style="top:196px"><p class="track__name">G. Varenne</p><p class="track__works">Op.41 Barcarolle No.2 G-Dur</p></div>
      <div class="track track__jp" style="top:236px"><p class="track__name">クヴィルンバッハ</p><p class="track__works">ヴェネチアの舟歌</p></div>
      <div class="track track__en" style="top:236px"><p class="track__name">F. Quirnbacher</p><p class="track__works">Venezianisches Gondellied II</p></div>
      <div class="track track__jp" style="top:275px"><p class="track__name">ゲルヴァト</p><p class="track__works">舟歌 Op.60 嬰ヘ長調</p></div>
      <div class="track track__en" style="top:275px"><p class="track__name">F. Gelvat</p><p class="track__works">Barcarolle Fis-Dur Op.60</p></div>
      <div class="track track__jp" style="top:315px"><p class="track__name">穂連みら</p><p class="track__works">海の伝説</p></div>
      <div class="track track__en" style="top:315px"><p class="track__name">Mira Hollen</p><p class="track__works">Legend of the Sea</p></div>
      <p class="contact">Mira Hollen<br>www.mirahollen.example</p>
    </div>
    <div class="front-panel">
      <div class="photo-portrait" role="img" aria-label="Foto: Porträt der Pianistin mit weißen Calla-Lilien im Vordergrund"></div>
      <p class="title title__kanji">～水～</p>
      <p class="title title__word title__word--serif">Water</p>
      <p class="artist artist__en">Klavier: Mira Hollen</p>
      <p class="artist artist__jp">ピアニスト　穂連みら</p>
      <div class="label"><span class="label__dot"></span>Mira Hollen</div>
      <p class="composers">Tumsat, Falkenor,<br>Varenne, Brokk,<br>Gelvat etc.</p>
      <p class="disc-number">01</p>
    </div>
  </section>

  <section class="spread spread--two">
    <div class="back-panel">
      <div class="photo-lake" role="img" aria-label="Foto: Pianistin im hellen Kleid liest Noten an einem Holzgeländer am nebligen See"></div>
      <div class="track track__jp" style="top:54px"><p class="track__name">ブロック</p><p class="track__works">エステ荘の噴水</p></div>
      <div class="track track__en" style="top:54px"><p class="track__name">F. Brokk</p><p class="track__works">Les jeux d'eaux à la Villa d'Este</p></div>
      <div class="track track__jp" style="top:93px"><p class="track__name">トゥムザット</p><p class="track__works">水の戯れ</p></div>
      <div class="track track__en" style="top:93px"><p class="track__name">M. Tumsat</p><p class="track__works">Jeux d'eau</p></div>
      <div class="track track__jp" style="top:133px"><p class="track__name">ファルケノール</p><p class="track__works">水の反映<br>雨の庭<br>金色の魚</p></div>
      <div class="track track__en" style="top:133px"><p class="track__name">C. Falkenor</p><p class="track__works">Reflets dans l'eau<br>Jardins sous la pluie<br>Poissons d'or</p></div>
      <div class="track track__jp" style="top:196px"><p class="track__name">ヴァレンヌ</p><p class="track__works">舟歌 第2番 ト長調</p></div>
      <div class="track track__en" style="top:196px"><p class="track__name">G. Varenne</p><p class="track__works">Op.41 Barcarolle No.2 G-Dur</p></div>
      <div class="track track__jp" style="top:236px"><p class="track__name">クヴィルンバッハ</p><p class="track__works">ヴェネチアの舟歌</p></div>
      <div class="track track__en" style="top:236px"><p class="track__name">F. Quirnbacher</p><p class="track__works">Venezianisches Gondellied II</p></div>
      <div class="track track__jp" style="top:275px"><p class="track__name">ゲルヴァト</p><p class="track__works">舟歌 Op.60 嬰ヘ長調</p></div>
      <div class="track track__en" style="top:275px"><p class="track__name">F. Gelvat</p><p class="track__works">Barcarolle Fis-Dur Op.60</p></div>
      <div class="track track__jp" style="top:315px"><p class="track__name">穂連みら</p><p class="track__works">海の伝説</p></div>
      <div class="track track__en" style="top:315px"><p class="track__name">Mira Hollen</p><p class="track__works">Legend of the Sea</p></div>
      <p class="contact">Mira Hollen<br>www.mirahollen.example</p>
    </div>
    <div class="front-panel">
      <div class="photo-portrait" role="img" aria-label="Foto: Porträt der Pianistin mit weißen Calla-Lilien im Vordergrund"></div>
      <p class="title title__kanji">～水～</p>
      <p class="title title__word title__word--caps">WATER</p>
      <p class="artist artist__en">Klavier: Mira Hollen</p>
      <p class="artist artist__jp">ピアニスト　穂連みら</p>
      <div class="label"><span class="label__dot"></span>Mira Hollen</div>
      <p class="composers">Tumsat, Falkenor,<br>Varenne, Brokk,<br>Gelvat etc.</p>
      <p class="disc-number">02</p>
    </div>
  </section>

</div>
</body>
</html>
```